Etikett für einen Rosé Wein
Zielgruppe
Wir sind ein Weingut und benötigen ein neues Etikett für unseren Muskattrollinger Rosé. Unsere Kunden sind eher traditionelle Weinkäufer.
Aufgabenstellung
Format:
Höhe: 9 cm
Breite: 11 cm
Da es nur ein Vorderetikett gibt, müssen alle relevanten Angaben (Hersteller, Alkohol, Inhalt in L, Rebsorte, etc.) enthalten sein. (siehe Flaschenabbildung anbei)
WÜRTTEMBERG
2019er
Muskattrollinger Rosé
DEUTSCHER QUALITÄTSWEIN
11,0 % Vol.
0,75 l
Enthält Sulfite
A.P.Nr. 58271346
Abfüller
Straße / PLZ / Ort / Tel.
Der Flaschenverschluss ist schwarz d.h. das neue Etikettendesign sollte dazu passen.
Bisher ist der Hintergrund des Weinetiketts schwarz. Dies muss jedoch nicht so bleiben.
Im Anhang finden Sie außerdem ein Plakat. Ggf. können Sie für das Flaschendesign einige nostalgische Elemente davon übernehmen.

```html
<!DOCTYPE html>
<html lang="de">
<head>
<meta charset="utf-8">
<title>Muskattrollinger Rosé – Etikett</title>
<link href="https://fonts.googleapis.com/css2?family=Quicksand:wght@500;600;700&display=swap" rel="stylesheet">
<style>
  :root {
    --backdrop: #dcdbdd;
    --label-paper: #f7f7f7;
    --ink: #1b1b1b;
    --wine: #a13a4a;
    --rule: #8a8a8a;
    --photo-sky: #d6d6d6;
    --photo-trees: #5a5a5a;
    --photo-field: #9a9a9a;
    --photo-vines: #6e6e6e;
    --seal: #e4e4e4;
  }
  * { margin: 0; padding: 0; box-sizing: border-box; }
  html, body { width: 1200px; height: 892px; overflow: hidden; }
  body {
    background: var(--backdrop);
    font-family: "Quicksand", sans-serif;
    color: var(--ink);
    position: relative;
  }
  .wine-label {
    position: absolute;
    left: 160px;
    top: 86px;
    width: 880px;
    height: 720px;
    background: var(--label-paper);
    box-shadow: 0 2px 10px rgba(0,0,0,0.12);
    overflow: hidden;
  }
  .seal-mark {
    position: absolute;
    right: 30px;
    top: 26px;
    width: 110px;
    height: 110px;
    border-radius: 50%;
    border: 2px solid var(--seal);
  }
  .region {
    position: absolute;
    top: 48px;
    width: 100%;
    text-align: center;
    font-weight: 600;
    font-size: 46px;
    line-height: 1;
    letter-spacing: 0.5px;
  }
  .vintage {
    position: absolute;
    top: 100px;
    width: 100%;
    text-align: center;
    font-weight: 600;
    font-size: 28px;
    line-height: 1;
  }
  .variety {
    position: absolute;
    top: 148px;
    width: 100%;
    text-align: center;
    font-weight: 500;
    font-size: 42px;
    line-height: 1;
    color: var(--wine);
  }
  .quality {
    position: absolute;
    top: 226px;
    left: 30px;
    width: 780px;
    text-align: center;
    font-weight: 600;
    font-size: 19px;
    letter-spacing: 0.3px;
  }
  .scene-photo {
    position: absolute;
    left: 30px;
    top: 262px;
    width: 780px;
    height: 390px;
    background: linear-gradient(180deg,
      var(--photo-sky) 0%, var(--photo-sky) 8%,
      var(--photo-trees) 14%, var(--photo-trees) 20%,
      var(--photo-field) 30%, var(--photo-field) 48%,
      var(--photo-vines) 64%, var(--photo-vines) 100%);
  }
  .facts-column {
    position: absolute;
    left: 818px;
    top: 262px;
    width: 40px;
    height: 390px;
    display: flex;
    flex-direction: column;
    border-left: 1px solid var(--rule);
    border-bottom: 1px solid var(--rule);
  }
  .fact {
    writing-mode: vertical-rl;
    transform: rotate(180deg);
    font-size: 13px;
    font-weight: 600;
    line-height: 1.2;
    text-align: center;
    display: flex;
    align-items: center;
    justify-content: center;
    border-bottom: 1px solid var(--rule);
    white-space: nowrap;
  }
  .fact:first-child { border-bottom: none; }
  .fact.approval { height: 130px; color: var(--wine); }
  .fact.bottler { height: 90px; }
  .fact.volume { height: 70px; }
  .fact.alcohol { height: 100px; }
  .producer-address {
    position: absolute;
    top: 670px;
    left: 0;
    width: 880px;
    text-align: center;
    font-size: 16px;
    font-weight: 600;
  }
</style>
</head>
<body>
  <main class="wine-label">
    <div class="seal-mark" aria-hidden="true"></div>
    <h1 class="region">WÜRTTEMBERG</h1>
    <p class="vintage">2019er</p>
    <h2 class="variety">Muskattrollinger Rosé</h2>
    <p class="quality">DEUTSCHER QUALITÄTSWEIN</p>
    <div class="scene-photo" role="img" aria-label="Schwarzweißfoto: Frau hält ein Glas Rotwein in einem Weinberg mit Rebzeilen und Bäumen im Hintergrund"></div>
    <div class="facts-column">
      <div class="fact approval">A.P.Nr. 58271346</div>
      <div class="fact bottler">Abfüller</div>
      <div class="fact volume">0,75 l</div>
      <div class="fact alcohol">11,0 % Vol.<br>Enthält Sulfite</div>
    </div>
    <p class="producer-address">Kelterweg 5 · D-74999 Rebenheim – Württemberg · Tel. 07100/2817364</p>
  </main>
</body>
</html>
```